Bright Horizon Website

Bright Horizon Advisory Services is a company which provides specialised advise in carbon markets, climate policy, landscapes, resilience and change. We are based in Australia but the majority of our business is global. Our clients range from governments to large corporates and not for profit organisations.
Our focus is on developing the capabilities of government officials, business decision makers and land managers so they can better navigate the complexity of climate change and sustainability.
We are looking for a website that is consistent with the high end professional services which we provide to serious players.
I have attached two versions of our logo. I have also attached the back of our business card so you can get a sense of what we hand to potential clients.

Target Market(s)

Professional individuals, decision makers, board members etc, government officials.

Industry/Entity Type

Government

Number of Pages Required

4 page

Font styles to use
Serif
Sans Serif

Requirements
Must have
• Please provide
• 1. Home page
• 2. Service page template
• 3. Contact page
• 4. Lead expert profile page

```html
<!DOCTYPE html>
<html lang="en">
<head>
<meta charset="utf-8">
<title>Bright Horizon – Contact</title>
<link href="https://fonts.googleapis.com/css2?family=Raleway:wght@300;400;500;600&display=swap" rel="stylesheet">
<style>
:root{
  --green:#82b053;
  --green-dark:#6b9a3b;
  --ink:#1e2226;
  --night:#1b2127;
  --text:#333;
  --muted:#7d8288;
  --panel:#f1f1f1;
  --white:#fff;
  --map-sea:#a7c7ee;
  --map-land:#e6e6c8;
}
*{box-sizing:border-box;margin:0;padding:0}
html,body{width:955px;height:1200px;overflow:hidden}
body{position:relative;background:var(--white);font-family:"Raleway",sans-serif;color:var(--text)}
.abs{position:absolute}
.topbar{left:0;top:0;width:955px;height:4px;background:var(--green)}
.topbar::before{content:"";position:absolute;left:0;top:0;width:296px;height:4px;background:var(--ink)}

.brand{left:38px;top:30px;display:flex;align-items:center;gap:12px}
.brand-dot{width:40px;height:40px;border-radius:50%;background:#8a8f94}
.brand-name{font-size:21px;font-weight:400;letter-spacing:2px;line-height:22px;color:#3b4045;text-transform:uppercase;width:150px}

.contact-top{right:62px;top:21px;text-align:right;font-size:9.5px;font-weight:300;color:#666;line-height:16px}
.contact-icons{left:905px;top:23px}

.nav{left:545px;top:55px;display:flex;align-items:center;font-size:11.5px;font-weight:500;color:var(--ink)}
.nav a{display:block;padding:0 10px;line-height:26px;color:inherit;text-decoration:none}
.nav a.current{background:var(--night);color:var(--white);padding:0 13px;border-top:2px solid var(--green);line-height:24px}

.band{left:0;top:108px;width:955px;height:81px;background:var(--green);color:var(--white);font-size:19.5px;font-weight:300;padding-left:157px;line-height:81px}

h2{position:absolute;font-size:18.5px;font-weight:400;color:#222}
.profile-photo{left:38px;top:284px;width:80px;height:111px;background:linear-gradient(160deg,#6f7b5a,#3a3e3d 55%,#c49a82 56%,#8d6b5b)}
.profile-links{left:38px;top:395px;width:80px;height:42px;background:var(--panel);display:flex;justify-content:center;align-items:center;gap:4px}
.profile-links span{width:22px;height:22px;border-radius:50%;background:#2d5a9c}
.bio{left:134px;top:280px;width:455px;font-size:10px;line-height:16.8px;font-weight:400;color:#333}
.bio p{margin-bottom:16.8px}

.map{left:635px;top:284px;width:239px;height:358px;background:linear-gradient(135deg,var(--map-sea) 0%,var(--map-land) 25%,var(--map-land) 70%,var(--map-sea) 92%)}
.office{left:635px;top:642px;width:239px;height:186px;background:var(--panel);padding:30px 25px;font-size:10px;line-height:12.2px;color:#222}
.office strong{display:block;font-size:11.5px;font-weight:600;line-height:13px}
.office p{margin-bottom:12px}

.footer{left:0;top:890px;width:955px;height:213px;background:var(--green-dark);color:var(--white)}
.footer .brand{left:37px;top:40px}
.footer .brand-dot{background:#d9e6c8}
.footer .brand-name{color:var(--white)}
.footer-rule{left:37px;top:104px;width:241px;height:1px;background:rgba(255,255,255,.25)}
.footer-address{left:89px;top:120px;font-size:8.7px;line-height:12px}
.footer-col{top:54px;font-size:9.7px}
.footer-col h3{font-size:9.7px;font-weight:600;color:#c6dcb0;margin-bottom:17px}
.footer-col li{list-style:none;line-height:16.7px;font-weight:400}
.socials{display:flex;gap:5px}
.socials span{width:21px;height:21px;border-radius:50%;background:rgba(255,255,255,.85)}

.base{left:0;top:1103px;width:955px;height:97px;background:var(--night);color:var(--muted);font-size:8.7px}
.legal{left:89px;top:26px}
.legal .sep{display:inline-block;width:1px;height:9px;background:#444;margin:0 10px;vertical-align:middle}
.copyright{left:89px;top:50px}
.subscribe-label{left:565px;top:16px;font-weight:600;font-size:9.5px;color:#555b61}
.subscribe-input{left:565px;top:34px;width:214px;height:27px;background:#a9adb1;color:#555;padding-left:8px;line-height:27px;font-size:9px}
.subscribe-btn{left:782px;top:34px;width:111px;height:27px;background:var(--green);color:var(--white);text-align:center;line-height:27px;font-size:13px;font-weight:500}
</style>
</head>
<body>
<div class="abs topbar"></div>

<header>
  <div class="abs brand"><span class="brand-dot"></span><span class="brand-name">Bright Horizon</span></div>
  <div class="abs contact-top">daniel.hartley@brighthorizon.example<br>+61 400 555 123</div>
  <svg class="abs contact-icons" width="12" height="30" viewBox="0 0 12 30">
    <rect x="1" y="1" width="10" height="7" fill="#82b053"/>
    <path d="M1 1 L6 5 L11 1" stroke="#fff" fill="none" stroke-width="1"/>
    <rect x="2.5" y="13" width="7" height="12" rx="1" stroke="#82b053" fill="none" stroke-width="1.3"/>
  </svg>
  <nav class="abs nav">
    <a class="current">Home</a><a>Our Mission</a><a>Our Services</a><a>About Us</a><a>Contact Us</a>
  </nav>
</header>

<div class="abs band">Please don’t hesitate to contact us for any enquiries you might have.</div>

<main>
  <h2 style="left:38px;top:237px">Daniel Hartley</h2>
  <div class="abs profile-photo" role="img" aria-label="Portrait photograph of Daniel Hartley"></div>
  <div class="abs profile-links"><span></span><span style="background:#2a9fd8"></span><span style="background:#1f7bb6"></span></div>
  <div class="abs bio">
    <p>Daniel Hartley is the lead advisor at Bright Horizon Advisory Services. He is recognised globally as an expert in climate policy, carbon markets, and their impact on business.</p>
    <p>Based in Melbourne, Australia, Daniel has provided advice to a wide range of organisations, including the Global Climate Secretariat, Australian and other governments, major corporations, international banks, service providers, industry associations and non-profit organisations. He is active in the design and implementation of carbon credit and trading schemes, development of market infrastructure, and the operation of existing carbon markets.</p>
    <p>Daniel has a unique perspective in this sphere, spanning the policy, regulation, commercial and technical aspects of carbon &amp; climate change. Daniel serves on a number of advisory boards, steering committees and decision making bodies in the carbon &amp; climate change space and he is a sought after speaker for domestic and international conferences and workshops.</p>
    <p>Daniel has been an active member of the Global Climate Secretariat’s expert register and has provided advice to the Offset Mechanism Board and other carbon market administrators on new methodologies, registration of projects and accreditation of verifiers. He is chair of the Technical Advisory Committee for the Verified Credit Foundation, and has contributed to the development of standards and protocols including the GCA Emissions Project Protocol, the international standard ISO14064, and the Australian Standard for carbon accounting in forests.</p>
  </div>

  <h2 style="left:632px;top:237px">Our Location</h2>
  <div class="abs map" role="img" aria-label="Map of Australia showing the office location in Melbourne"></div>
  <div class="abs office">
    <p><strong>BRIGHT HORIZON</strong>Level 4, 120 Harbour Rd Docklands<br>Victoria 3008 Melbourne, Australia</p>
    <p>Phone<br>Tel: +61 3 9000 1000<br>Fax: +61 3 9000 3222</p>
    <p>Email<br>daniel.hartley@brighthorizon.example</p>
  </div>
</main>

<footer class="abs footer">
  <div class="abs brand"><span class="brand-dot"></span><span class="brand-name">Bright Horizon</span></div>
  <div class="abs footer-rule"></div>
  <div class="abs footer-address">Level 4, 120 Harbour Rd<br>Docklands Victoria 3008<br>Melbourne, Australia<br>Tel: +61 3 9000 1000<br>Fax: +61 3 9000 3222</div>
  <div class="abs footer-col" style="left:339px">
    <h3>Who We Are</h3>
    <ul><li>Home</li><li>Our Mission</li><li>About Us</li><li>Press Release</li><li>Contact Us</li></ul>
  </div>
  <div class="abs footer-col" style="left:459px">
    <h3>What We Do</h3>
    <ul><li>Corporate Advisory on Carbon Market</li><li>Project Mechanisms (Carbon Credits &amp; Offsets)</li><li>Monitoring, Reporting &amp; Verification</li><li>Institutional Arrangements</li><li>Training &amp; Coaching</li><li>China’s Carbon Markets</li></ul>
  </div>
  <div class="abs footer-col" style="left:748px">
    <h3>Get Social</h3>
    <div class="socials"><span></span><span></span><span></span><span></span><span></span></div>
  </div>
</footer>

<div class="abs base">
  <div class="abs legal">Sitemap<span class="sep"></span>Privacy Policy</div>
  <div class="abs copyright">Copyright © 2014 Bright Horizon</div>
  <div class="abs subscribe-label">Subscribe Email Newsletter</div>
  <div class="abs subscribe-input">Email</div>
  <div class="abs subscribe-btn">Submit</div>
</div>
</body>
</html>
```